promotional flyer for Valtera Gym

we are after a double sided a5 leaflet to promote our gym, this is to go out to the general public to entice them into getting membership.

gym membership is £30 per month

it should also include the offer of - if you present this leaflet then there will be no joining fee

some of the features of the gym include

strength machines
cardio machines
functional area
sprung floor mat area

Target Market(s)

Adults 16+ who want to go to the gym and workout

Industry/Entity Type

Gym

Font styles to use
Other font styles liked:
• montserrat Regular

Requirements
Must have
• Clean on brand design
• use images supplied by us
Nice to have
• focus on an inclusive experience as the gym will be advertised to everyone
• should also use our "fitter, stronger, Healthier"

```html
<!DOCTYPE html>
<html lang="en">
<head>
<meta charset="utf-8">
<title>Valtera Gym – A5 Leaflet</title>
<link href="https://fonts.googleapis.com/css2?family=Bebas+Neue&family=Montserrat:wght@400;500;600;700&display=swap" rel="stylesheet">
<style>
  :root {
    --stage: #858a55;
    --orange: #ec6a43;
    --orange-deep: #dd5a31;
    --orange-box: #ee5b2b;
    --slate: #4a5f6b;
    --slate-dark: #2e3c45;
    --ink: #3a4650;
    --white: #ffffff;
  }
  * { margin: 0; padding: 0; box-sizing: border-box; }
  html, body { width: 1200px; height: 1200px; overflow: hidden; }
  body { background: var(--stage); font-family: "Montserrat", sans-serif; position: relative; }

  .flyer { position: absolute; top: 259px; width: 476px; height: 681px; overflow: hidden; }
  .flyer--front { left: 97px; }
  .flyer--back { left: 627px; }
  .flyer__bg { position: absolute; inset: 0; width: 100%; height: 100%; }
  .abs { position: absolute; }
  .centered { transform: translate(-50%, -50%); text-align: center; white-space: nowrap; }

  /* brand lockup */
  .brand__dot { position: absolute; border-radius: 50%; background: var(--orange); }
  .brand__name { font-weight: 400; letter-spacing: 0.06em; text-transform: uppercase; }
  .brand__tag { font-weight: 600; color: var(--orange); letter-spacing: 0.12em; text-transform: uppercase; }

  /* front */
  .headline { font-family: "Bebas Neue", sans-serif; color: var(--white); font-size: 62px; line-height: 1; }
  .dash-rule { position: absolute; left: 261px; width: 182px; border-top: 1px dashed rgba(255,255,255,0.85); }
  .cta-title { font-weight: 700; color: var(--white); font-size: 26px; line-height: 1; }
  .rule { position: absolute; height: 2px; background: var(--white); }
  .price-label { color: var(--white); font-size: 20px; font-weight: 500; }
  .price { color: var(--white); font-size: 50px; font-weight: 700; line-height: 1; }
  .join-btn {
    position: absolute; left: 266px; top: 518px; width: 172px; height: 36px;
    background: var(--slate-dark); border-radius: 3px; color: var(--white);
    font-weight: 600; font-size: 21px; display: flex; align-items: center; justify-content: center;
  }
  .offer { position: absolute; left: 245px; top: 572px; width: 215px; text-align: center; color: var(--white); font-size: 14px; line-height: 18px; font-weight: 500; }
  .contact-line { display: flex; align-items: center; gap: 4px; color: var(--white); font-weight: 500; white-space: nowrap; }
  .contact-line svg { flex: none; }

  /* back */
  .panel { position: absolute; left: 17px; top: 347px; width: 443px; height: 211px; background: var(--orange-box); border-radius: 4px; }
  .panel__heading { position: absolute; left: 10px; color: var(--white); font-weight: 600; font-size: 22px; line-height: 1; }
  .features { position: absolute; left: 12px; top: 40px; width: 420px; display: grid; grid-template-columns: 221px 1fr; row-gap: 8px; list-style: none; }
  .features li { display: flex; align-items: center; gap: 7px; color: var(--white); font-size: 15px; line-height: 17px; }
  .about { position: absolute; left: 10px; top: 122px; width: 426px; color: var(--white); font-size: 10px; line-height: 12.3px; text-align: justify; font-weight: 500; }
  .contact-title { color: var(--white); font-weight: 700; font-size: 19px; letter-spacing: 0.02em; }
  .address { position: absolute; left: 30px; top: 619px; color: var(--white); font-size: 12px; line-height: 13.5px; font-weight: 500; }
</style>
</head>
<body>

<!-- FRONT -->
<section class="flyer flyer--front">
  <svg class="flyer__bg" viewBox="0 0 595 851" preserveAspectRatio="none">
    <defs>
      <linearGradient id="gymFloor" x1="0" y1="0" x2="0.4" y2="1">
        <stop offset="0" stop-color="#7a3a2c"/>
        <stop offset="0.35" stop-color="#a8452d"/>
        <stop offset="0.7" stop-color="#3b3436"/>
        <stop offset="1" stop-color="#2a2a2e"/>
      </linearGradient>
    </defs>
    <rect width="595" height="851" fill="#ffffff"/>
    <polygon role="img" aria-label="Photo: woman lifting dumbbells in the gym weights area" points="0,96 595,291 595,851 0,851" fill="url(#gymFloor)"/>
    <polygon points="0,711 595,466 595,851 0,851" fill="var(--slate)"/>
    <rect x="306" y="0" width="269" height="851" fill="var(--orange)"/>
    <polygon points="306,581 575,470 575,851 306,851" fill="var(--orange-deep)"/>
  </svg>

  <div class="brand__dot" style="left:118px; top:29px; width:22px; height:22px;"></div>
  <div class="abs centered brand__name" style="left:129px; top:71px; font-size:16px; color:var(--ink);">Valtera Gym</div>
  <div class="abs centered brand__tag" style="left:129px; top:85px; font-size:5.5px;">Fitter | Stronger | Healthier</div>

  <div class="abs centered headline" style="left:352px; top:57px;">Fitter</div>
  <div class="dash-rule" style="top:86px;"></div>
  <div class="abs centered headline" style="left:352px; top:121px;">Stronger</div>
  <div class="dash-rule" style="top:154px;"></div>
  <div class="abs centered headline" style="left:352px; top:185px;">Healthier</div>

  <div class="abs centered cta-title" style="left:352px; top:358px;">Become a</div>
  <div class="abs centered cta-title" style="left:352px; top:385px;">member</div>
  <div class="rule" style="left:316px; top:402px; width:72px;"></div>

  <div class="abs centered price-label" style="left:352px; top:426px;">Gym membership</div>
  <div class="abs centered price" style="left:352px; top:461px;">£30</div>
  <div class="abs centered price-label" style="left:352px; top:493px;">per month</div>

  <div class="join-btn">join today !</div>

  <p class="offer">it should also include the offer of - if you present this leaflet then there will be no joining fee</p>

  <div class="abs contact-line" style="left:18px; top:601px; font-size:15px;">
    <svg width="12" height="12" viewBox="0 0 24 24"><path fill="var(--orange)" d="M6.6 10.8a15.1 15.1 0 0 0 6.6 6.6l2.2-2.2a1 1 0 0 1 1-.25 11.4 11.4 0 0 0 3.6.57 1 1 0 0 1 1 1V20a1 1 0 0 1-1 1A17 17 0 0 1 3 4a1 1 0 0 1 1-1h3.5a1 1 0 0 1 1 1c0 1.25.2 2.45.57 3.6a1 1 0 0 1-.25 1z"/></svg>
    +44 1632 960418
  </div>
  <div class="abs contact-line" style="left:18px; top:623px; font-size:15px;">
    <svg width="12" height="12" viewBox="0 0 24 24" fill="none" stroke="var(--orange)" stroke-width="2"><circle cx="12" cy="12" r="10"/><path d="M2 12h20M12 2a15 15 0 0 1 0 20M12 2a15 15 0 0 0 0 20"/></svg>
    www.valteragym.co.uk
  </div>
</section>

<!-- BACK -->
<section class="flyer flyer--back">
  <svg class="flyer__bg" viewBox="0 0 595 851" preserveAspectRatio="none">
    <defs>
      <linearGradient id="spinRoom" x1="0" y1="0" x2="1" y2="1">
        <stop offset="0" stop-color="#3e4650"/>
        <stop offset="0.4" stop-color="#5a4f55"/>
        <stop offset="0.7" stop-color="#8a5a3e"/>
        <stop offset="1" stop-color="#4a3a38"/>
      </linearGradient>
    </defs>
    <rect width="595" height="851" fill="var(--slate)"/>
    <polygon role="img" aria-label="Photo: two women riding spin bikes in front of a painted mural" points="0,0 180,0 595,145 595,310 310,434 0,560" fill="url(#spinRoom)"/>
    <polygon points="330,434 595,320 595,560 420,560" fill="#6b5f5c"/>
  </svg>

  <div class="brand__dot" style="left:395px; top:20px; width:20px; height:20px;"></div>
  <div class="abs centered brand__name" style="left:406px; top:54px; font-size:12px; color:var(--white);">Valtera Gym</div>
  <div class="abs centered brand__tag" style="left:406px; top:64px; font-size:4px;">Fitter | Stronger | Healthier</div>

  <div class="panel">
    <h2 class="panel__heading" style="top:9px;">Features of the gym</h2>
    <div class="rule" style="left:10px; top:33px; width:83px;"></div>
    <ul class="features">
      <li><svg width="13" height="13" viewBox="0 0 24 24"><circle cx="12" cy="12" r="11" fill="#fff"/><path d="M6.5 12.5l3.5 3.5 7.5-7.5" fill="none" stroke="var(--orange-box)" stroke-width="3"/></svg>Strength machines</li>
      <li><svg width="13" height="13" viewBox="0 0 24 24"><circle cx="12" cy="12" r="11" fill="#fff"/><path d="M6.5 12.5l3.5 3.5 7.5-7.5" fill="none" stroke="var(--orange-box)" stroke-width="3"/></svg>Functional area</li>
      <li><svg width="13" height="13" viewBox="0 0 24 24"><circle cx="12" cy="12" r="11" fill="#fff"/><path d="M6.5 12.5l3.5 3.5 7.5-7.5" fill="none" stroke="var(--orange-box)" stroke-width="3"/></svg>Cardio machines</li>
      <li><svg width="13" height="13" viewBox="0 0 24 24"><circle cx="12" cy="12" r="11" fill="#fff"/><path d="M6.5 12.5l3.5 3.5 7.5-7.5" fill="none" stroke="var(--orange-box)" stroke-width="3"/></svg>Sprung floor mat area</li>
    </ul>
    <h2 class="panel__heading" style="top:92px; font-size:20px;">About us</h2>
    <div class="rule" style="left:10px; top:114px; width:54px;"></div>
    <p class="about">Valtera is the brainchild of medal winning Judo competitor Dan Hollis and well-known fitness guru Tara Quinn. Tara has been a personal trainer in the area for a number of years helping many clients achieve their goals, one of those clients was Dan who was training for a big judo competition, after building a successful training partnership the pair began to pursue the dream of setting up Valtera, a name the pair chose to stand for "best".</p>
  </div>

  <div class="abs centered contact-title" style="left:238px; top:587px;">CONTACT US</div>
  <div class="rule" style="left:196px; top:602px; width:84px;"></div>

  <svg class="abs" style="left:17px; top:620px;" width="9" height="12" viewBox="0 0 24 32"><path fill="var(--orange)" d="M12 0a11 11 0 0 0-11 11c0 8 11 21 11 21s11-13 11-21A11 11 0 0 0 12 0zm0 15a4 4 0 1 1 0-8 4 4 0 0 1 0 8z"/></svg>
  <p class="address">Unit 4, harbour parade, Mill Ave,<br>Westbrook, Kentham<br>KT9 2LP, UK</p>

  <div class="abs contact-line" style="left:252px; top:617px; font-size:12px;">
    <svg width="10" height="10" viewBox="0 0 24 24"><path fill="var(--orange)" d="M6.6 10.8a15.1 15.1 0 0 0 6.6 6.6l2.2-2.2a1 1 0 0 1 1-.25 11.4 11.4 0 0 0 3.6.57 1 1 0 0 1 1 1V20a1 1 0 0 1-1 1A17 17 0 0 1 3 4a1 1 0 0 1 1-1h3.5a1 1 0 0 1 1 1c0 1.25.2 2.45.57 3.6a1 1 0 0 1-.25 1z"/></svg>
    +44 1632 960418
  </div>
  <div class="abs contact-line" style="left:252px; top:634px; font-size:12px;">
    <svg width="10" height="10" viewBox="0 0 24 24" fill="none" stroke="var(--orange)" stroke-width="2"><circle cx="12" cy="12" r="10"/><path d="M2 12h20M12 2a15 15 0 0 1 0 20M12 2a15 15 0 0 0 0 20"/></svg>
    www.valteragym.co.uk
  </div>
</section>

</body>
</html>
```